Dentistry

Dentist's personal business card. No logo needed. The card shoul deliver the massage of reliability, professionalism, experience.
Please ad the full brief of the project: down the line it says: the winning look should be precise and pristine NO pictures of Teeth, smiles, instruments etc.

The details to be desplaid are:
Dr. Rob Valdoni
Doctor of Dental Surgery
PHD
Web. Www.drvaldoni.com
Email. Rob@drvaldoni.com
Tel 07731482590
Surgery address. 27Bharwick road London SW4 7QN UK
82 Fenwyn Row London SW3 2HT. Uk

Reason: Decided to make the payment unrefundable in order to get more designers involved.

Requirements
Should not have
• Logo, teeth, smile any sort of instruments.

```html
<!DOCTYPE html>
<html lang="en">
<head>
<meta charset="utf-8">
<title>Dr. Rob Valdoni — Business Card</title>
<link rel="stylesheet" href="https://fonts.googleapis.com/css2?family=Open+Sans:wght@300;400;600;700&display=swap">
<style>
  :root {
    --card-bg: #ffffff;
    --red-deep: #a82720;
    --red-bright: #de2a28;
    --red-low: #b3231e;
    --name-red: #8e1b17;
    --title-red: #9c1f1a;
    --text-grey: #6a6a6a;
    --label-grey: #5f5f5f;
  }
  * { margin: 0; padding: 0; box-sizing: border-box; }
  html, body {
    width: 1200px; height: 667px; overflow: hidden;
    background: var(--card-bg);
  }
  .card {
    position: relative; width: 1200px; height: 667px;
    background: var(--card-bg);
    font-family: "Open Sans", sans-serif;
    overflow: hidden;
  }
  .accent-field { position: absolute; inset: 0; width: 1200px; height: 667px; }

  .identity { position: absolute; left: 689px; top: 80px; }
  .identity__name {
    font-size: 38px; font-weight: 700; color: var(--name-red);
    line-height: 52px; letter-spacing: -0.2px;
  }
  .identity__title {
    font-size: 33px; font-weight: 300; color: var(--title-red);
    line-height: 52px; letter-spacing: -0.3px;
  }

  .contact__row {
    position: absolute; left: 689px;
    font-size: 23px; line-height: 38px; color: var(--text-grey);
    white-space: nowrap; letter-spacing: -0.3px;
  }
  .contact__label { font-weight: 600; color: var(--label-grey); }
  .contact__icon {
    position: absolute; left: -50px; top: 7px;
    width: 24px; height: 24px; fill: var(--text-grey);
  }
  .contact__row--address { top: 357px; }
  .contact__row--phone { top: 469px; }
  .contact__row--email { top: 544px; }

  .website {
    position: absolute; left: 46px; top: 600px;
    font-size: 27px; line-height: 36px; font-weight: 400;
    color: var(--text-grey); letter-spacing: -0.2px;
  }
</style>
</head>
<body>
<main class="card">
  <svg class="accent-field" viewBox="0 0 1200 667" preserveAspectRatio="none" role="img" aria-label="Soft red colour field along the left side of the card">
    <defs>
      <linearGradient id="field-red" x1="0" y1="0" x2="0" y2="1">
        <stop offset="0" stop-color="var(--red-deep)"/>
        <stop offset="0.5" stop-color="var(--red-bright)"/>
        <stop offset="1" stop-color="var(--red-low)"/>
      </linearGradient>
    </defs>
    <path fill="url(#field-red)" d="M0,0 L470,0 C500,220 560,440 580,667 L0,667 Z"/>
  </svg>

  <header class="identity">
    <h1 class="identity__name">Dr. Rob Valdoni</h1>
    <p class="identity__title">Doctor of Dental Surgery</p>
    <p class="identity__title">PHD</p>
  </header>

  <section class="contact">
    <p class="contact__row contact__row--address">
      <svg class="contact__icon" viewBox="0 0 24 24" aria-hidden="true"><path d="M12 3 L2 12 H5 V21 H10 V15 H14 V21 H19 V12 H22 Z"/></svg>
      <span class="contact__label">Address:</span> 27Bharwick road London SW4<br>7QN UK 82 Fenwyn Row London SW3 2HT. Uk
    </p>
    <p class="contact__row contact__row--phone">
      <svg class="contact__icon" viewBox="0 0 24 24" aria-hidden="true"><path d="M6.6 2.5 L9.5 6.4 L7.7 8.8 C9 11.8 12 14.8 15.2 16.3 L17.6 14.5 L21.5 17.4 L19.6 20.6 C12 21 3 12 3.4 4.4 Z"/></svg>
      <span class="contact__label">Ph:</span> 07731482590
    </p>
    <p class="contact__row contact__row--email">
      <svg class="contact__icon" viewBox="0 0 24 24" aria-hidden="true"><path d="M12 2 A10 10 0 1 0 12.01 2 Z M4.5 8 H19.5 V10 H4.5 Z M3.5 12 H20.5 V14 H3.5 Z M4.8 16 H19.2 V17.6 H4.8 Z"/></svg>
      <span class="contact__label">Email:</span> Rob@drvaldoni.com
    </p>
  </section>

  <p class="website">www.drvaldoni.com</p>
</main>
</body>
</html>
```